Glam By Nora

I am a makeup artist looking for professional looking double sided business card. I would like to create a logo and incorporate a set of eyes as the periods above the name "Nora" on the card.

front of card: Logo "Glow by Nora" written across diagonal (bottom left to top right)

Back of card:
1) Professional makeup artist serving New York & New Jersey (or similar to this text)
2) 917-555-0148
3) glowbynora@lumavex.com

```html
<!DOCTYPE html>
<html lang="en">
<head>
<meta charset="utf-8">
<title>Glow by Nora – Business Card</title>
<link href="https://fonts.googleapis.com/css2?family=Poppins:wght@500&display=swap" rel="stylesheet">
<style>
  :root {
    --canvas: #ece8e1;
    --royal: #3137d6;
    --periwinkle: #6e73ea;
    --lilac: #b3b6f5;
    --teal: #5fe3e0;
    --teal-light: #8ff0ec;
    --rose: #e8336b;
    --ink: #1a1a1a;
    --paper: #ffffff;
  }
  * { margin: 0; padding: 0; box-sizing: border-box; }
  html, body { width: 1200px; height: 1000px; overflow: hidden; }
  body {
    background: var(--canvas);
    font-family: "Poppins", sans-serif;
    position: relative;
  }
  .card {
    position: absolute;
    width: 537px;
    height: 323px;
    border-radius: 28px;
    overflow: hidden;
    box-shadow: 0 0 0 2px #9aa0b8, 0 6px 14px rgba(0,0,0,0.25);
  }
  .card--front {
    left: 145px; top: 147px;
    background: radial-gradient(ellipse 380px 230px at 68% 50%, var(--lilac) 0%, var(--periwinkle) 55%, var(--royal) 100%);
  }
  .card--back {
    left: 518px; top: 520px;
    background: linear-gradient(135deg, var(--royal) 0%, var(--periwinkle) 60%, var(--lilac) 100%);
  }
  .eyes-art {
    position: absolute;
    left: 282px; top: 50px;
    width: 236px; height: 92px;
    border-radius: 46px;
    background: radial-gradient(ellipse at 50% 55%, rgba(95,227,224,0.75) 0%, rgba(60,120,160,0.55) 45%, rgba(26,26,40,0.25) 75%, rgba(26,26,40,0) 100%);
  }
  .brand-name {
    position: absolute;
    left: 48px; top: 142px;
    font-size: 50px;
    font-weight: 500;
    color: var(--rose);
    line-height: 1;
    letter-spacing: 0.5px;
  }
  .info-band {
    position: absolute;
    left: 0; right: 0;
    top: 262px;
    height: 38px;
    background: linear-gradient(90deg, var(--teal) 0%, var(--teal-light) 50%, var(--teal) 100%);
    display: flex;
    align-items: center;
    font-size: 16.5px;
    color: var(--ink);
  }
  .card--front .info-band { justify-content: center; padding-right: 12px; }
  .base-strip {
    position: absolute;
    left: 0; right: 0; bottom: 0;
    height: 21px;
    background: linear-gradient(90deg, var(--lilac), #9a9df2);
  }
  .photo-panel {
    position: absolute;
    left: 13px; top: 13px;
    width: 511px; height: 243px;
    background: var(--paper);
    clip-path: polygon(22px 0, 489px 0, 511px 30px, 511px 100%, 0 100%, 0 30px);
  }
  .card--back .info-band {
    justify-content: space-between;
    padding: 0 30px 0 38px;
    font-size: 15px;
  }
  .contact { display: flex; align-items: center; gap: 6px; }
  .contact-icon { width: 20px; height: 20px; }
  .at-mark { font-size: 18px; font-weight: 500; }
  .card--back .base-strip {
    left: 6px; right: 8px; bottom: 8px; height: 14px;
    clip-path: polygon(0 0, 100% 0, 99% 100%, 1% 100%);
  }
</style>
</head>
<body>
  <section class="card card--front" aria-label="Business card front">
    <div class="eyes-art" role="img" aria-label="Illustration area: pair of stylised made-up eyes with brows and lashes"></div>
    <h1 class="brand-name">Glow by Nora</h1>
    <p class="info-band">Professional makeup artist serving New York &amp; New Jersey</p>
    <div class="base-strip"></div>
  </section>

  <section class="card card--back" aria-label="Business card back">
    <div class="photo-panel" role="img" aria-label="Blank white writing panel"></div>
    <div class="info-band">
      <span class="contact">
        <svg class="contact-icon" viewBox="0 0 24 24" aria-hidden="true">
          <path d="M6.6 2.5l3 3.2-1.8 2.4c1.2 2.6 3.4 4.9 6.1 6.1l2.4-1.8 3.2 3-1.9 3.8C10.2 18.8 5.2 13.8 3 6.4z" fill="none" stroke="#1a1a1a" stroke-width="2" stroke-linejoin="round"/>
        </svg>
        917-555-0148
      </span>
      <span class="contact"><span class="at-mark">@</span> glowbynora@lumavex.com</span>
    </div>
    <div class="base-strip"></div>
  </section>
</body>
</html>
```